Business card design and logo for plumbing bussiness

We are wanting a logo for a plumbing business is Queensland Australia. KRV Plumbing and Drainage will be doing works on domestic and commercial sites.
Plumbing, drainage and gas works. We are wanting something that will stand out and be noticed. Colours could be black blue and white but open for suggestions.

Target Market(s)

Builders and home renovators

Industry/Entity Type

Plumbing

Contact Information for Business Card

Miles Dorgan - Director
0417 582 913
miles@krvplumbing.example.com.au
QBCC: 847 2106
ABN: 52 319 407 281

Font styles to use
Sans Serif

Colors
000000

Requirements
Must have
• Clear defined branding

```html
<!DOCTYPE html>
<html lang="en">
<head>
<meta charset="utf-8">
<title>KRV Plumbing and Drainage – Business Card</title>
<link rel="stylesheet" href="https://fonts.googleapis.com/css2?family=Lato:wght@400;700&family=Montserrat:wght@600;700&display=swap">
<style>
  :root {
    --stage: #2b2b2b;
    --card: #000000;
    --blue: #4a7cc0;
    --white: #ffffff;
  }
  * { box-sizing: border-box; margin: 0; padding: 0; }
  html, body { width: 1200px; height: 680px; overflow: hidden; }
  body {
    background: var(--stage);
    display: flex;
    align-items: center;
    justify-content: center;
    gap: 40px;
    font-family: "Lato", Arial, sans-serif;
  }
  .card {
    position: relative;
    width: 540px;
    height: 330px;
    background: var(--card);
    overflow: hidden;
    box-shadow: 0 10px 30px rgba(0,0,0,.45);
  }
  .brand {
    position: absolute;
    display: flex;
    align-items: center;
    gap: 12px;
    color: var(--white);
    font-family: "Montserrat", Arial, sans-serif;
    font-weight: 700;
    text-transform: uppercase;
    line-height: 1.02;
  }
  .brand-dot { flex: none; border-radius: 50%; background: var(--blue); }
  .card-front .brand { left: 34px; top: 48px; font-size: 17px; letter-spacing: .5px; }
  .card-front .brand-dot { width: 16px; height: 16px; }
  .brand-name { display: block; font-size: 1.9em; letter-spacing: 2px; margin-bottom: 2px; }

  .person { position: absolute; right: 48px; top: 62px; text-align: right; }
  .person-name {
    font-family: "Montserrat", Arial, sans-serif;
    font-weight: 600;
    font-size: 24px;
    color: var(--blue);
  }
  .person-role { font-size: 13px; color: var(--white); margin-top: 2px; }

  .divider {
    position: absolute;
    left: 30px; right: 40px; top: 158px;
    height: 1px;
    background: var(--blue);
  }
  .contact {
    position: absolute;
    display: flex;
    align-items: center;
    gap: 9px;
    color: var(--white);
    letter-spacing: .3px;
  }
  .contact svg { flex: none; }
  .contact-phone { left: 34px; top: 190px; font-size: 17px; }
  .contact-email { right: 40px; top: 192px; font-size: 14px; }

  .licence-band {
    position: absolute;
    left: 0; right: 0; bottom: 0;
    height: 42px;
    background: var(--blue);
    display: flex;
    align-items: center;
    justify-content: flex-end;
    padding: 0 40px;
    color: var(--white);
    font-size: 14px;
    letter-spacing: .3px;
  }

  .card-back { display: flex; align-items: center; justify-content: center; }
  .card-back .brand { position: static; font-size: 24px; letter-spacing: .8px; gap: 16px; }
  .card-back .brand-dot { width: 22px; height: 22px; }
</style>
</head>
<body>

<section class="card card-front" aria-label="Business card front">
  <div class="brand">
    <span class="brand-dot"></span>
    <span><span class="brand-name">KRV</span>Plumbing<br>and Drainage</span>
  </div>

  <div class="person">
    <p class="person-name">Miles Dorgan</p>
    <p class="person-role">Director</p>
  </div>

  <div class="divider"></div>

  <p class="contact contact-phone">
    <svg width="14" height="14" viewBox="0 0 24 24" aria-hidden="true"><path fill="#4a7cc0" d="M6.6 10.8a15.1 15.1 0 0 0 6.6 6.6l2.2-2.2c.3-.3.7-.4 1-.2 1.1.4 2.3.6 3.6.6.6 0 1 .4 1 1V20c0 .6-.4 1-1 1C10.6 21 3 13.4 3 4c0-.6.4-1 1-1h3.5c.6 0 1 .4 1 1 0 1.3.2 2.5.6 3.6.1.3 0 .7-.2 1z"/></svg>
    0417 582 913
  </p>
  <p class="contact contact-email">
    <svg width="15" height="11" viewBox="0 0 15 11" aria-hidden="true"><rect x="0.5" y="0.5" width="14" height="10" fill="#4a7cc0"/><path d="M1 1l6.5 5L14 1" fill="none" stroke="#000" stroke-width="1.2"/></svg>
    miles@krvplumbing.example.com.au
  </p>

  <p class="licence-band">QBCC: 847 2106 &bull; ABN: 52 319 407 281</p>
</section>

<section class="card card-back" aria-label="Business card back">
  <div class="brand">
    <span class="brand-dot"></span>
    <span><span class="brand-name">KRV</span>Plumbing<br>and Drainage</span>
  </div>
</section>

</body>
</html>
```